今回のチラシは当社が年4回発行している会報誌に同梱し、DMで直接お客様へ届けるものになります。
対象は庭付一戸建てに住まわれているお客様がほとんどです。なので、セールスワード(安い、お得、今だけ、限定、キャンペーンなど)をちりばめたようなギラギラしたチラシではなく、当社がお客様のお悩みから解放します的な心情に訴えるチラシにしたいです。
お客様のお困りの原因としては、お勤めでなかなか草むしりする時間が取れない、少し前までは自分でやっていたが年で体力的に難しくなった、奥様がマメに手入れしていたが他界してしまい手つかず状態、親が他界して家を相続したが自分は庭に興味なし。お隣さんから苦情が来てしまう。などなど様々です。
庭木が無くても雑草で困っている方にも、気兼ねなく当社にご依頼してもらえるようなイメージのチラシにしたいです。

トップページ
https://www.574k.co.jp/
除草
https://www.574k.co.jp/weeding/
砂利敷き(防草シート含む)
https://www.574k.co.jp/gravel/
表面:キャッチコピー、キャッチコピーに合う写真などの組合せ※情報はこの2つにしてシンプルに。
裏面:社名、支払い方法、フリーダイヤル、URL、QRコードなど ※添付資料参照
A4
両面
シンプル 複雑
単色 カラフル
暗い 明るい
日常 高級
遊び心 厳粛
未来的 伝統的
女性的 男性的
黄・オレンジ系、緑系、茶系
• イラストレーター形式 (.ai)
印刷用のPDFも納品ください。

情報量を少なくしシンプルにまとまっている。
お客様のお困りごとを端的に示していて伝わりやすい。
裏面にある商品説明の記載内容は必要十分の情報量で綺麗に整理されていて読みやすい。

皆様、この度は弊社のチラシ作成に応募いただき誠にありがとうございました。
社内で投票を行いましたが、どれかに集中することなく票がばらける程どれも良い感じだったと思います。
またチラシ作成やその他で募集させていただく際は是非ご応募ください。

```html
<!DOCTYPE html>
<html lang="ja">
<head>
<meta charset="utf-8">
<title>除草だけでもOK! 庭守工房</title>
<link href="https://fonts.googleapis.com/css2?family=M+PLUS+Rounded+1c:wght@500;800;900&family=Noto+Sans+JP:wght@500;700;900&display=swap" rel="stylesheet">
<style>
:root{
  --green:#2f9a3a;
  --green-dark:#1f6e28;
  --green-light:#8cc63f;
  --red:#e5261b;
  --orange:#f39a1e;
  --orange-deep:#ee7d14;
  --white:#ffffff;
  --ink:#333333;
  --cream:#fffbe9;
}
*{margin:0;padding:0;box-sizing:border-box}
html,body{width:846px;height:1200px;overflow:hidden;background:#fff}
body{font-family:"Noto Sans JP",sans-serif;color:var(--ink)}
.flyer{position:relative;width:846px;height:1200px;overflow:hidden;background:#fff}

.hero-photo{position:absolute;left:0;top:0;width:846px;height:780px;
  background:linear-gradient(180deg,#cfe3c2 0%,#a9cc8e 35%,#6f9d4e 70%,#4d7a38 100%)}
.people-photo{position:absolute;left:130px;top:300px;width:620px;height:420px;
  background:radial-gradient(ellipse at 30% 45%,#f3d6c4 0%,#e4b9a0 30%,transparent 60%),
             radial-gradient(ellipse at 72% 45%,#f0cfbd 0%,#d9a88d 30%,transparent 60%)}
.gardener-illust{position:absolute;left:20px;top:170px;width:150px;height:190px;border-radius:8px;
  background:linear-gradient(180deg,#dfe8e0,#b9c9b8)}

.badge-garden{position:absolute;left:18px;top:12px;width:150px;height:150px;border-radius:50%;
  background:var(--red);border:4px solid var(--white);display:flex;flex-direction:column;
  align-items:center;justify-content:center;color:var(--white);
  font-family:"M PLUS Rounded 1c",sans-serif;font-weight:900;font-size:33px;line-height:1.15;
  box-shadow:0 3px 6px rgba(0,0,0,.25)}

.catch-sub{position:absolute;left:180px;top:36px;font-family:"M PLUS Rounded 1c",sans-serif;
  font-weight:900;font-size:56px;color:var(--red);
  -webkit-text-stroke:10px var(--white);paint-order:stroke fill;letter-spacing:1px}

.catch-main{position:absolute;left:196px;top:96px;width:580px;height:180px}
.catch-weed{position:absolute;left:0;top:30px;padding:0 10px;background:rgba(255,255,255,.9);
  border-radius:10px;font-family:"M PLUS Rounded 1c",sans-serif;font-weight:900;font-size:136px;
  line-height:150px;color:var(--green);-webkit-text-stroke:3px var(--green-dark)}
.catch-only{position:absolute;left:315px;top:0;padding:2px 12px;background:var(--white);border-radius:8px;
  font-family:"M PLUS Rounded 1c",sans-serif;font-weight:900;font-size:46px;color:var(--red)}
.catch-ok{position:absolute;left:330px;top:56px;font-family:"M PLUS Rounded 1c",sans-serif;font-weight:900;
  font-size:110px;color:var(--green);-webkit-text-stroke:12px var(--white);paint-order:stroke fill}
.pill-weeding{position:absolute;left:80px;top:185px;padding:4px 30px;background:var(--green);
  border:3px solid var(--white);border-radius:30px;color:var(--white);font-weight:900;font-size:36px;
  font-family:"M PLUS Rounded 1c",sans-serif}

.sigh{position:absolute;left:668px;top:420px;color:var(--white);font-size:26px;font-weight:700;transform:rotate(-10deg)}

.trouble-title{position:absolute;left:0;width:846px;top:518px;text-align:center;color:var(--white);
  font-family:"M PLUS Rounded 1c",sans-serif;font-weight:900;font-size:44px;
  text-shadow:0 2px 6px rgba(0,0,0,.55)}
.trouble-list{position:absolute;left:70px;top:590px;width:706px;display:flex;justify-content:space-between;list-style:none}
.trouble-list li{width:126px;height:126px;border-radius:50%;background:var(--green);border:4px solid var(--white);
  display:flex;align-items:center;justify-content:center;text-align:center;color:var(--white);
  font-weight:900;font-size:22px;line-height:1.3;box-shadow:0 2px 6px rgba(0,0,0,.3)}
.trouble-note{position:absolute;left:0;width:846px;top:728px;text-align:center;color:var(--white);
  font-weight:900;font-size:24px;text-shadow:0 1px 4px rgba(0,0,0,.6)}

.contact-band{position:absolute;left:0;top:780px;width:846px;height:200px;background:linear-gradient(180deg,var(--orange),var(--orange-deep))}
.offer-box{position:absolute;left:30px;top:16px;width:786px;height:66px;background:var(--cream);border-radius:8px;
  text-align:center;font-family:"M PLUS Rounded 1c",sans-serif;font-weight:900;font-size:46px;line-height:66px;color:var(--red)}
.tel-row{position:absolute;left:30px;top:96px;width:786px;height:94px;display:flex;align-items:center;gap:16px}
.freecall{display:flex;flex-direction:column;align-items:center;width:100px;flex:none;color:var(--white);font-size:15px;font-weight:700}
.freecall-mark{width:62px;height:62px;background:var(--white);margin-bottom:4px}
.tel-number{flex:none;font-family:"Noto Sans JP",sans-serif;font-weight:900;font-size:72px;color:var(--white);letter-spacing:0;line-height:1;white-space:nowrap}
.hours{margin-left:auto;flex:none;align-self:flex-end;padding-bottom:6px;color:var(--white);font-weight:700;font-size:20px;text-align:right;line-height:1.2;white-space:nowrap}
.hours b{display:block;font-size:28px;font-weight:900}

.footer{position:absolute;left:0;top:980px;width:846px;height:220px;background:#fff}
.operator-photo{position:absolute;left:30px;top:14px;width:130px;height:190px;border-radius:8px;
  background:linear-gradient(180deg,#eef2f4,#c8d3da)}
.bubble{position:absolute;left:185px;top:44px;width:150px;height:110px;border-radius:50%;background:#f3f3f3;
  border:3px solid var(--green-light);display:flex;align-items:center;justify-content:center;text-align:center;
  font-weight:700;font-size:22px;line-height:1.35;color:var(--ink)}
.brand{position:absolute;left:380px;top:34px;display:flex;flex-direction:column}
.brand-en{font-weight:700;font-size:20px;letter-spacing:4px;color:var(--green)}
.brand-name{display:flex;align-items:center;gap:14px;font-weight:900;font-size:78px;color:var(--green);line-height:1.1}
.brand-name i{display:block;width:22px;height:22px;border-radius:50%;background:var(--green-light)}
.address{position:absolute;left:380px;top:176px;font-size:13px;color:#666;line-height:1.4}
</style>
</head>
<body>
<main class="flyer">
  <section class="hero">
    <div class="hero-photo" role="img" aria-label="雑草の茂る庭を背景に、電話する笑顔の女性と草むしりに疲れた女性の写真"></div>
    <div class="people-photo" role="img" aria-label="二人の女性の人物写真"></div>
    <div class="gardener-illust" role="img" aria-label="庭仕事をする作業員のイラスト"></div>

    <div class="badge-garden"><span>お庭の</span><span>お手入れ</span></div>
    <p class="catch-sub">手に負えない!</p>
    <h1 class="catch-main">
      <span class="catch-weed">除草</span>
      <span class="catch-only">だけでも</span>
      <span class="catch-ok">OK!</span>
      <span class="pill-weeding">草むしり</span>
    </h1>
    <span class="sigh">あぁ~</span>

    <h2 class="trouble-title">こんな困った!を解決!</h2>
    <ul class="trouble-list">
      <li>体力的に<br>キツイ</li>
      <li>手入れ<br>する人<br>いない</li>
      <li>雑草が<br>増え<br>すぎた</li>
      <li>このまま<br>じゃ●●<br>迷惑に</li>
      <li>放置も<br>できない</li>
    </ul>
    <p class="trouble-note">庭木なくても雑草で困っている方や草むしりでもOKです!</p>
  </section>

  <section class="contact-band">
    <p class="offer-box">除草作業だけでも承ります!</p>
    <div class="tel-row">
      <div class="freecall"><span class="freecall-mark"></span>フリーコール</div>
      <p class="tel-number">0120-574-108</p>
      <p class="hours">受付時間<b>9:00~18:00</b></p>
    </div>
  </section>

  <footer class="footer">
    <div class="operator-photo" role="img" aria-label="電話対応する女性スタッフの写真"></div>
    <p class="bubble">お問い合せは<br>お気軽に</p>
    <div class="brand">
      <span class="brand-en">NIWAMORI KOBO</span>
      <span class="brand-name"><i></i>庭守工房</span>
    </div>
    <p class="address">〒000-0000 緑区庭町1-2-3<br>営業 月~土 定休日 日曜・祝日</p>
  </footer>
</main>
</body>
</html>
```